The Lantern Circle

I need a design for a 1 page flyer but also a brochure

Target Market(s)

Wealthy, elegant, intelligent, discerning women who are on a journey of self-discovery.

Industry/Entity Type

Spiritual and personal development, yoga, meditation

Requirements
Must have
• Be very elegant, attractive, upmarket minimalist but also bit mystical
Nice to have
• I would like to use my logo (see uploaded file). The texts are also uploaded. One for the 1 page flyer 1 for a full brochure
Should not have
• be too busy, multicoloured, garish.

```html
<!DOCTYPE html>
<html lang="en">
<head>
<meta charset="utf-8">
<title>The Lantern Circle — Retreat Flyer</title>
<link rel="stylesheet" href="https://fonts.googleapis.com/css2?family=Barlow:ital,wght@0,400;0,500;0,600;0,700;1,400;1,500&family=Barlow+Condensed:wght@300;400;600;700&display=swap">
<style>
  :root {
    --green: #0f4d2a;
    --green-dark: #0a3c20;
    --charcoal: #3d3d3f;
    --ink: #4a4a4c;
    --paper: #f1f2f2;
    --panel: #e4e5e6;
    --page-bg: #d9d9d9;
    --white: #ffffff;
  }
  * { box-sizing: border-box; margin: 0; padding: 0; }
  html, body { width: 1125px; height: 1200px; overflow: hidden; }
  body {
    background: var(--page-bg);
    font-family: "Barlow", Arial, sans-serif;
    color: var(--ink);
    position: relative;
  }
  .flyer {
    position: absolute;
    left: 114px; top: 20px;
    width: 896px; height: 1160px;
    background: linear-gradient(135deg, #f6f7f7 0%, #eceded 45%, #f7f8f8 60%, #e9eaea 100%);
    overflow: hidden;
  }
  .hero-photo {
    position: absolute; left: 0; top: 0; width: 896px; height: 421px;
    background: linear-gradient(180deg, #f1e4dc 0%, #e9e3e2 35%, #c9d2d8 58%, #8f9ba4 78%, #5f5a57 100%);
  }
  .brand-mark {
    position: absolute; left: 718px; top: 65px; width: 111px; height: 111px;
    background: rgba(255,255,255,0.55);
    border: 1px solid rgba(255,255,255,0.8);
    display: flex; flex-direction: column; align-items: center; justify-content: center; gap: 10px;
  }
  .brand-mark .dot { width: 26px; height: 26px; border-radius: 50%; background: var(--green); }
  .brand-mark .name {
    font-family: "Barlow", Arial, sans-serif; font-size: 11px; font-weight: 500;
    color: var(--green); text-align: center; line-height: 1.2; letter-spacing: 0.5px;
  }
  .tagline-band {
    position: absolute; left: 368px; top: 345px; width: 528px; height: 46px;
    background: rgba(40,40,42,0.72);
    color: var(--white);
    font-family: "Barlow Condensed", Arial, sans-serif; font-weight: 400; font-size: 31px;
    line-height: 46px; padding-left: 12px; letter-spacing: 0.5px;
  }
  .date-tag {
    position: absolute; left: 413px; top: 394px; width: 415px; height: 46px;
    background: var(--green); color: var(--white);
    font-family: "Barlow Condensed", Arial, sans-serif; font-weight: 700; font-size: 26px;
    line-height: 46px; text-align: center; letter-spacing: 0.3px;
    clip-path: polygon(10px 0, 100% 0, 100% calc(100% - 10px), calc(100% - 10px) 100%, 0 100%, 0 10px);
  }
  .title-block {
    position: absolute; left: 66px; top: 172px; width: 299px; height: 298px;
    background: var(--green);
    clip-path: polygon(0 14px, 14px 0, 230px 0, 299px 70px, 299px 284px, 285px 298px, 14px 298px, 0 284px);
    padding: 36px 0 0 36px;
  }
  .title-block h1 {
    font-family: "Barlow Condensed", Arial, sans-serif; font-weight: 600;
    font-size: 70px; line-height: 73px; color: var(--white); letter-spacing: 0.5px;
  }
  .intro-panel {
    position: absolute; left: 66px; top: 463px; width: 352px; height: 192px;
    background: var(--panel);
    clip-path: polygon(0 0, 100% 0, 100% calc(100% - 14px), calc(100% - 14px) 100%, 14px 100%, 0 calc(100% - 14px));
  }
  .intro-panel p {
    position: absolute; left: 38px; top: 30px; width: 290px;
    font-style: italic; font-weight: 500; font-size: 17px; line-height: 22px; color: #3a3a3c;
  }
  .intro-panel .rule {
    position: absolute; left: 38px; top: 160px; width: 36px; height: 3px; background: var(--green);
  }
  .section-tag {
    position: absolute; height: 32px;
    background: var(--green); color: var(--white);
    font-weight: 600; font-size: 16px; line-height: 32px; padding-left: 14px;
    clip-path: polygon(0 0, calc(100% - 8px) 0, 100% 8px, 100% 100%, 0 100%);
  }
  .check-list { position: absolute; list-style: none; }
  .check-list li {
    position: relative; padding-left: 20px;
    font-size: 14px; line-height: 22px; color: var(--ink);
  }
  .check-list li::before {
    content: ""; position: absolute; left: 0; top: 6px;
    width: 10px; height: 10px; border: 1.3px solid var(--green); border-radius: 50%;
  }
  .check-list li::after {
    content: ""; position: absolute; left: 3.5px; top: 8.5px;
    width: 2.5px; height: 4px; border: solid var(--green); border-width: 0 1.3px 1.3px 0;
    transform: rotate(45deg);
  }
  .body-copy { position: absolute; font-size: 13.5px; line-height: 20px; color: var(--ink); }
  .venue-name {
    position: absolute; left: 471px; top: 704px;
    font-weight: 700; font-size: 14px; color: var(--green);
  }
  .reserve-back {
    position: absolute; left: 471px; top: 929px; width: 358px; height: 146px;
    background: var(--green);
    clip-path: polygon(0 0, calc(100% - 14px) 0, 100% 14px, 100% calc(100% - 14px), calc(100% - 14px) 100%, 0 100%);
  }
  .reserve-card {
    position: absolute; left: 487px; top: 897px; width: 326px; height: 101px;
    background: var(--charcoal); color: var(--white);
    padding: 12px 0 0 27px;
    clip-path: polygon(0 0, 100% 0, 100% calc(100% - 14px), calc(100% - 14px) 100%, 0 100%);
  }
  .reserve-card h2 { font-size: 17px; font-weight: 600; line-height: 22px; margin-bottom: 4px; }
  .reserve-card p { font-size: 13px; line-height: 18px; font-weight: 500; }
  .contact {
    position: absolute; left: 487px; display: flex; align-items: center; gap: 12px;
    color: var(--white); font-size: 19px; font-weight: 500;
  }
  .contact svg { width: 18px; height: 18px; }
  .footer-band {
    position: absolute; left: 0; top: 1119px; width: 896px; height: 41px; background: var(--charcoal);
  }
  .footer-tab {
    position: absolute; left: 166px; top: 1102px; width: 562px; height: 40px;
    background: var(--charcoal);
    clip-path: polygon(14px 0, calc(100% - 14px) 0, 100% 14px, 100% 100%, 0 100%, 0 14px);
  }
  .footer-quote {
    position: absolute; left: 0; top: 1115px; width: 896px; text-align: center;
    color: var(--white); font-style: italic; font-weight: 500; font-size: 19px;
  }
</style>
</head>
<body>
<main class="flyer">
  <div class="hero-photo" role="img" aria-label="Photo of a woman meditating cross-legged on a beach at dusk beside a stack of balanced stones"></div>

  <div class="brand-mark">
    <span class="dot"></span>
    <span class="name">THE LANTERN<br>CIRCLE</span>
  </div>

  <div class="tagline-band">PATHWAYS TO OUR TRUE ESSENCE</div>
  <div class="date-tag">TUSCANY, ITALY — 25-29 JUNE 2026</div>

  <div class="title-block"><h1>THE<br>LANTERN<br>CIRCLE</h1></div>

  <div class="intro-panel">
    <p>A refined, intimate journey into inner quiet, energetic awakening, and embodied presence — held within the beauty and serenity of a private Tuscan villa.</p>
    <span class="rule"></span>
  </div>

  <div class="section-tag" style="left:66px;top:691px;width:230px;">What You Will Experience</div>
  <ul class="check-list" style="left:78px;top:868px;top:868px;top:868px;top:868px;top:868px;top:868px;top:868px;top:868px;top:868px;top:735px;">
    <li>Energetic activation &amp; exploration</li>
    <li>Meditation &amp; breathwork</li>
    <li>Somatic movement &amp; intuitive embodiment</li>
    <li>Shadow exploration</li>
    <li>Sound &amp; frequency immersion</li>
    <li>Reiki healing</li>
    <li>Forest bathing</li>
    <li>Craftwork to soothe the nervous system</li>
  </ul>

  <div class="section-tag" style="left:66px;top:938px;width:258px;">Why This Retreat Is Different</div>
  <p class="body-copy" style="left:66px;top:982px;width:350px;">This is not a yoga retreat — though yoga informs the work. It is a deeply personalised, spacious, and elegant invitation to return to your essence. With only 5–8 participants, each guest receives individualised attention, intuitive guidance, and profound holding.</p>

  <div class="section-tag" style="left:471px;top:472px;width:157px;">What’s Included</div>
  <ul class="check-list" style="left:474px;top:515px;">
    <li>4 nights luxury accommodation</li>
    <li>All practices, workshops, and guidance</li>
    <li>Plant-based meals</li>
    <li>Energy &amp; Reiki sessions</li>
    <li>Craftwork materials</li>
    <li>Forest bathing experience</li>
  </ul>

  <div class="section-tag" style="left:471px;top:664px;width:99px;">Location</div>
  <div class="venue-name">Villa Serenella, Tuscany</div>
  <p class="body-copy" style="left:471px;top:727px;width:340px;">A serene historic villa surrounded by rolling hills, ancient trees, and luminous Tuscan light — an ideal setting for restoration and inner exploration.</p>

  <div class="section-tag" style="left:471px;top:802px;width:84px;">Pricing</div>
  <p class="body-copy" style="left:471px;top:845px;width:340px;">Pricing varies by room selection. Full pricing sheet available upon request.</p>

  <div class="reserve-back"></div>
  <div class="reserve-card">
    <h2>Reserve Your Place</h2>
    <p>Limited to 5–8 participants.<br>A brief call ensures the retreat aligns with<br>your intentions.</p>
  </div>
  <div class="contact" style="top:1010px;">
    <svg viewBox="0 0 18 18" fill="none" stroke="#fff" stroke-width="1.4"><rect x="1.5" y="3.5" width="15" height="11"/><path d="M1.5 4l7.5 6 7.5-6"/></svg>
    <span>mara@the-lantern-circle.com</span>
  </div>
  <div class="contact" style="top:1041px;">
    <svg viewBox="0 0 18 18" fill="none" stroke="#fff" stroke-width="1.4"><path d="M4 2l3 3-1.5 2.5c1 2 2.5 3.5 4.5 4.5L12.5 10.5l3 3-2 2.5C8 15.5 2.5 10 2 4.5z"/></svg>
    <span>+41 79 482 15 30</span>
  </div>

  <div class="footer-band"></div>
  <div class="footer-tab"></div>
  <p class="footer-quote">“Step into your essence… and emerge transformed.”</p>
</main>
</body>
</html>
```